Dark Comedy Movie Poster

We need a poster design for our short film BRAM that we just wrapped on.
It's a dark comedy
Bram explores the world of loneliness through the lens of a manic man-child. Bram wants nothing more than the approval of others, giving every last bit of energy to the cause. But his ravenous attempts accomplish the opposite, turning others off. His desperation is authentic, his lonliness cavernous.
Here is a link to the film
https://clipvault.example/548207316
Password: Bram42
I want you, the artist, to pitch me an idea in any way you want. I'm open to absolutely anything right now. Once I have some pitches from you all my production team and I will sort through them and pick the best fit!
-Owen

```html
<!DOCTYPE html>
<html lang="en">
<head>
<meta charset="utf-8">
<title>BRAM — Poster</title>
<link href="https://fonts.googleapis.com/css2?family=Bodoni+Moda:opsz,wght@6..96,500&family=Oswald:wght@400;500&display=swap" rel="stylesheet">
<style>
  :root {
    --backdrop: #e6e4e0;
    --paper: #c8bb99;
    --title-brown: #7a4630;
    --credit-brown: #6b3f2c;
    --scene-dark: #1e1712;
    --scene-warm: #4a3626;
    --plush-cream: #e9e2d6;
    --plush-tan: #b58e63;
  }
  html, body {
    margin: 0;
    width: 1200px;
    height: 1148px;
    overflow: hidden;
    background: var(--backdrop);
  }
  .poster {
    position: absolute;
    left: 250px;
    top: 74px;
    width: 700px;
    height: 1000px;
    background: var(--paper);
    overflow: hidden;
  }
  .film-still {
    position: absolute;
    left: 0;
    top: 0;
    width: 700px;
    height: 440px;
    background:
      radial-gradient(ellipse at 40% 55%, rgba(150,110,70,0.55), transparent 55%),
      radial-gradient(ellipse at 80% 50%, rgba(90,70,90,0.45), transparent 50%),
      linear-gradient(180deg, var(--scene-dark), var(--scene-warm));
  }
  .torn-edge {
    position: absolute;
    left: 0;
    top: 260px;
    width: 700px;
    height: 200px;
  }
  .plush-toy {
    position: absolute;
    left: 270px;
    top: 540px;
    width: 160px;
    height: 150px;
    border-radius: 45% 45% 35% 35%;
    background: radial-gradient(ellipse at 50% 45%, var(--plush-cream) 40%, var(--plush-tan) 85%, transparent 72%);
  }
  .title {
    position: absolute;
    left: 0;
    right: 0;
    top: 660px;
    margin: 0;
    text-align: center;
    font-family: "Bodoni Moda", serif;
    font-weight: 500;
    font-size: 190px;
    line-height: 1;
    letter-spacing: -4px;
    color: var(--title-brown);
  }
  .credits {
    position: absolute;
    left: 70px;
    right: 70px;
    top: 868px;
    font-family: "Oswald", sans-serif;
    color: var(--credit-brown);
    text-transform: uppercase;
  }
  .credit-row {
    display: flex;
    justify-content: center;
    gap: 14px;
    margin-bottom: 8px;
  }
  .credit {
    display: flex;
    align-items: center;
    gap: 4px;
  }
  .credit-role {
    font-size: 6px;
    line-height: 1.05;
    text-align: right;
    width: 42px;
  }
  .credit-name {
    font-size: 14px;
    font-weight: 500;
    white-space: nowrap;
  }
</style>
</head>
<body>
  <main class="poster">
    <div class="film-still" role="img" aria-label="Film still: a man in a dim candle-lit room crowded with teddy bears and colourful string lights"></div>
    <svg class="torn-edge" viewBox="0 0 700 200" preserveAspectRatio="none" aria-hidden="true">
      <path fill="#c8bb99" d="M0 40 C40 30 70 48 110 52 L130 58 150 56 180 70 210 74 240 90 270 96 300 112 330 118 360 122 380 128 410 120 440 112 470 104 500 96 530 90 560 82 600 74 640 70 670 66 700 62 L700 200 L0 200 Z"/>
    </svg>
    <div class="plush-toy" role="img" aria-label="Cream and tan plush puppy toy with a ribbon bow, sitting upright"></div>
    <h1 class="title">BRAM</h1>
    <section class="credits">
      <div class="credit-row">
        <div class="credit"><span class="credit-role">Produced by</span><span class="credit-name">Marisa Quell , Toby Renfield</span></div>
        <div class="credit"><span class="credit-role">Executive producers</span><span class="credit-name">Hedda Lorne, Curtis Vale</span></div>
        <div class="credit"><span class="credit-role">Starring</span><span class="credit-name">Wade Ellery, Jonah Pike</span></div>
      </div>
      <div class="credit-row">
        <div class="credit"><span class="credit-role">Director of photography</span><span class="credit-name">Ansel R. Dorn</span></div>
        <div class="credit"><span class="credit-role">Editor</span><span class="credit-name">Curtis Vale</span></div>
        <div class="credit"><span class="credit-role">Production design</span><span class="credit-name">Lucinda Marsh , Ivy Castell</span></div>
      </div>
    </section>
  </main>
</body>
</html>
```